Relocation/furniture installation company needs new business cards

we are a relocation and furniture installation company mainly dealing with corporate clients and we are looking for new business card ideas. Cards should incorporate our logo and list our website, phone number and services. The company is only 2 years old but with more staff joining we are in the need for more business cards, so something with an awesome design that is eye catching would go a long way to insure we get our name out there and look good to potential new clients.

Target Market(s)

Corporate

Industry/Entity Type

Trade

Contact Information for Business Card

www.mervoline.co.nz
0508 4 bravok

furniture installation
business relocations
joinery installation
commercial property maintenance

Colors
0592cd
34a7d8
85cae6
85acd3
0356a4
cfdfed
cee9f5
757575
474747

Requirements
Must have
• Business relocations and furniture installation specialists
Nice to have
• something that incorporates our logo.

```html
<!DOCTYPE html>
<html lang="en">
<head>
<meta charset="utf-8">
<title>Mervoline business cards</title>
<link rel="stylesheet" href="https://fonts.googleapis.com/css2?family=Exo+2:wght@600;700&display=swap">
<style>
  :root{
    --backdrop:#2a2a2a;
    --card:#ffffff;
    --navy:#2b3f9e;
    --royal:#0356a4;
    --sky:#85cae6;
    --cyan:#34a7d8;
    --grey-dark:#474747;
    --rule:#b9b9b9;
  }
  *{box-sizing:border-box;margin:0;padding:0}
  html,body{width:1200px;height:873px;overflow:hidden}
  body{
    background:var(--backdrop);
    font-family:"Exo 2",sans-serif;
    position:relative;
  }
  .card{
    position:absolute;
    width:540px;height:309px;
    background:var(--card);
    border-radius:22px;
    overflow:hidden;
  }
  .card--front{left:40px;top:282px}
  .card--back{left:620px;top:282px}
  .card__bands{position:absolute;inset:0;width:100%;height:100%}
  .band--navy{fill:var(--navy)}
  .band--royal{fill:var(--royal)}
  .band--sky{fill:var(--sky)}
  .band--grey{fill:var(--grey-dark)}

  .wordmark{
    position:absolute;left:0;right:0;
    text-align:center;
    font-weight:700;
    color:var(--navy);
    letter-spacing:3px;
    line-height:1;
  }
  .card--front .wordmark{top:134px;font-size:36px}
  .card--back .wordmark{top:72px;font-size:36px}

  .rule{position:absolute;height:1px;background:var(--rule)}
  .rule--top{left:110px;right:60px;top:118px}
  .rule--bottom{left:60px;right:110px;top:176px}

  .contact{
    position:absolute;left:0;right:0;top:126px;
    text-align:center;font-weight:700;line-height:20px;
  }
  .contact__phone{color:var(--navy);font-size:16px;letter-spacing:1px;text-transform:uppercase}
  .contact__web{color:var(--cyan);font-size:14px;letter-spacing:.5px;text-transform:uppercase}

  .services{
    position:absolute;left:40px;right:40px;top:184px;
    text-align:center;color:var(--navy);
    font-weight:600;font-size:13px;line-height:22px;
    white-space:nowrap;
  }
  .services__dot{color:var(--cyan);padding:0 4px}
</style>
</head>
<body>

<section class="card card--front">
  <svg class="card__bands" viewBox="0 0 540 309" aria-hidden="true">
    <polygon class="band--navy" points="0,160 100,110 0,220"/>
    <polygon class="band--sky" points="0,220 100,110 125,110 40,309 0,309"/>
    <polygon class="band--grey" points="40,309 125,110 140,110 70,309"/>
    <polygon class="band--navy" points="540,149 440,199 540,89"/>
    <polygon class="band--sky" points="540,89 440,199 415,199 500,0 540,0"/>
    <polygon class="band--grey" points="500,0 415,199 400,199 470,0"/>
  </svg>
  <div class="wordmark">MERVOLINE</div>
</section>

<section class="card card--back">
  <svg class="card__bands" viewBox="0 0 540 309" aria-hidden="true">
    <polygon class="band--navy" points="0,170 120,125 0,195"/>
    <polygon class="band--sky" points="0,195 120,125 140,125 0,225"/>
    <polygon class="band--grey" points="0,225 140,125 152,125 0,240"/>
    <polygon class="band--grey" points="540,175 540,205 470,250 462,240"/>
    <polygon class="band--sky" points="540,215 540,255 440,309 390,309"/>
    <polygon class="band--royal" points="540,255 540,290 500,309 440,309"/>
  </svg>
  <div class="wordmark">MERVOLINE</div>
  <div class="rule rule--top"></div>
  <div class="contact">
    <p class="contact__phone">0508 4 bravok</p>
    <p class="contact__web">www.mervoline.co.nz</p>
  </div>
  <div class="rule rule--bottom"></div>
  <div class="services">
    <p>Furniture installation<span class="services__dot">•</span>Business relocations<span class="services__dot">•</span>Joinery installation</p>
    <p>Commercial property maintenance</p>
  </div>
</section>

</body>
</html>
```